Marlow Ridge Dental business card

Business card would have following info:

Alden R. Kasprzak, DMD, FAGD
General Dentist
email: office@marlowridgedental.example
phone: 617-490-3867
fax: 617-490-3867
website: marlowridgedental.example

second side would have lines for:

appointment date
appointment time

```html
<!DOCTYPE html>
<html lang="en">
<head>
<meta charset="utf-8">
<title>Marlow Ridge Dental – Business Card</title>
<link href="https://fonts.googleapis.com/css2?family=Arimo:wght@400;700&display=swap" rel="stylesheet">
<style>
  :root {
    --navy: #0d4a86;
    --navy-deep: #0a3566;
    --cyan: #0aa3d5;
    --ink: #3a3a3a;
    --rule: #6b6b6b;
    --paper: #fbfbfb;
    --backdrop: #e4e4e4;
  }
  * { margin: 0; padding: 0; box-sizing: border-box; }
  html, body { width: 1200px; height: 801px; overflow: hidden; }
  body {
    background: radial-gradient(ellipse at 45% 35%, #f2f2f2 0%, var(--backdrop) 75%);
    font-family: "Arimo", Arial, sans-serif;
    position: relative;
  }
  .card {
    position: absolute;
    top: 252px;
    width: 520px;
    height: 298px;
    background: var(--paper);
    box-shadow: 0 6px 18px rgba(0,0,0,0.18);
    overflow: hidden;
  }
  .card--front { left: 50px; }
  .card--back { left: 630px; }

  /* Front */
  .brand {
    position: absolute;
    display: flex;
    align-items: center;
    gap: 12px;
  }
  .brand__mark {
    width: 34px; height: 34px; border-radius: 50%;
    background: var(--cyan);
  }
  .brand__name { font-size: 30px; font-weight: 400; color: var(--navy); letter-spacing: 0.5px; }
  .card--front .brand { top: 46px; left: 108px; }
  .divider {
    position: absolute; left: 40px; right: 40px; top: 128px;
    height: 1px; background: var(--rule);
  }
  .dentist { position: absolute; left: 40px; top: 146px; }
  .dentist__name { font-size: 18px; font-weight: 700; color: var(--cyan); }
  .dentist__role { font-size: 15px; color: var(--ink); margin-top: 4px; }
  .dentist__rule { width: 200px; height: 1px; background: var(--rule); margin-top: 8px; }
  .contacts { list-style: none; margin-top: 8px; }
  .contacts li {
    display: flex; align-items: center; gap: 8px;
    font-size: 14px; color: var(--ink); line-height: 20px;
  }
  .contacts svg { width: 13px; height: 13px; fill: var(--cyan); flex: none; }

  /* Back */
  .band {
    position: absolute; left: 0; top: 0; width: 100%; height: 126px;
    background: linear-gradient(100deg, var(--navy-deep) 0%, var(--navy) 60%, #0f4f8c 100%);
  }
  .band__line { position: absolute; left: 0; top: 126px; width: 100%; height: 3px; background: var(--cyan); }
  .card--back .brand { top: 40px; left: 70px; }
  .card--back .brand__name { color: #ffffff; }
  .tab { position: absolute; left: 60px; top: 126px; width: 360px; height: 34px; }
  .tab__label {
    position: absolute; left: 60px; top: 128px; width: 360px; text-align: center;
    font-size: 19px; color: #ffffff; letter-spacing: 1px; line-height: 30px;
  }
  .dashed { position: absolute; left: 28px; right: 28px; top: 178px; border-top: 1px dashed #9a9a9a; }
  .days {
    position: absolute; left: 28px; right: 28px; top: 200px;
    display: flex; justify-content: space-between;
  }
  .option { display: flex; align-items: center; gap: 8px; font-size: 16px; color: var(--ink); }
  .checkbox { width: 13px; height: 13px; border: 2px solid var(--cyan); }
  .schedule {
    position: absolute; left: 28px; right: 28px; top: 244px;
    display: flex; align-items: flex-end; gap: 10px; font-size: 16px; color: var(--ink);
  }
  .blank { border-bottom: 1px solid var(--ink); height: 16px; }
  .blank--date { width: 130px; }
  .blank--time { width: 90px; }
  .schedule .option { margin-left: 12px; }
</style>
</head>
<body>

<section class="card card--front" aria-label="Card front">
  <div class="brand">
    <span class="brand__mark"></span>
    <span class="brand__name">Marlow Ridge Dental</span>
  </div>
  <div class="divider"></div>
  <div class="dentist">
    <p class="dentist__name">Alden R. Kasprzak, DMD, FAGD</p>
    <p class="dentist__role">General Dentist</p>
    <div class="dentist__rule"></div>
    <ul class="contacts">
      <li><svg viewBox="0 0 24 24" aria-label="Phone"><path d="M6.6 10.8a15 15 0 0 0 6.6 6.6l2.2-2.2a1 1 0 0 1 1-.25 11.4 11.4 0 0 0 3.6.57 1 1 0 0 1 1 1V20a1 1 0 0 1-1 1A17 17 0 0 1 3 4a1 1 0 0 1 1-1h3.5a1 1 0 0 1 1 1c0 1.25.2 2.45.57 3.6a1 1 0 0 1-.25 1z"/></svg>617-490-3867</li>
      <li><svg viewBox="0 0 24 24" aria-label="Fax"><path d="M6 2h9l3 3v5H6zM3 11h18v9H3zm3 3v2h4v-2zm9 0v2h3v-2z"/></svg>617-490-3867</li>
      <li><svg viewBox="0 0 24 24" aria-label="Email"><path d="M2 5h20v14H2zm2 2v.5l8 5 8-5V7l-8 5z"/></svg>office@marlowridgedental.example</li>
      <li><svg viewBox="0 0 24 24" aria-label="Website"><circle cx="12" cy="12" r="10"/></svg>www.marlowridgedental.example</li>
    </ul>
  </div>
</section>

<section class="card card--back" aria-label="Card back">
  <div class="band"></div>
  <div class="band__line"></div>
  <div class="brand">
    <span class="brand__name">Marlow Ridge Dental</span>
  </div>
  <svg class="tab" viewBox="0 0 360 34" preserveAspectRatio="none" aria-hidden="true">
    <polygon points="0,0 360,0 345,30 15,30" fill="var(--cyan)"/>
  </svg>
  <p class="tab__label">APPOINTMENT</p>
  <div class="dashed"></div>
  <div class="days">
    <span class="option"><span class="checkbox"></span>MON</span>
    <span class="option"><span class="checkbox"></span>TUE</span>
    <span class="option"><span class="checkbox"></span>WED</span>
    <span class="option"><span class="checkbox"></span>THU</span>
    <span class="option"><span class="checkbox"></span>FRI</span>
    <span class="option"><span class="checkbox"></span>SAT</span>
  </div>
  <div class="schedule">
    <span>DATE</span><span class="blank blank--date"></span>
    <span>TIME</span><span class="blank blank--time"></span>
    <span class="option"><span class="checkbox"></span>AM</span>
    <span class="option"><span class="checkbox"></span>PM</span>
  </div>
</section>

</body>
</html>
```